Brindle Gardenworks Business Card

An eye catching, yet simple business card that includes;

1. our logo
2. office phone - 5127730194
3. email - brindlegardenworks@mailnest.example
4. website - www.brindlegardenworks.example
5. instagram - @brindlegardenworksrvt

```html
<!DOCTYPE html>
<html lang="en">
<head>
<meta charset="utf-8">
<title>Brindle Gardenworks Business Card</title>
<link rel="stylesheet" href="https://fonts.googleapis.com/css2?family=Open+Sans:wght@400;700;800&display=swap">
<style>
  :root {
    --bg: #5e5e5e;
    --card: #ffffff;
    --copper: #a05f28;
    --ink: #1d1917;
    --text: #222222;
  }
  * { margin: 0; padding: 0; box-sizing: border-box; }
  html, body { width: 1200px; height: 780px; overflow: hidden; }
  body {
    background: var(--bg);
    font-family: "Open Sans", sans-serif;
    position: relative;
  }
  .card {
    position: absolute;
    top: 230px;
    width: 540px;
    height: 320px;
    background: var(--card);
    border-radius: 18px;
    overflow: hidden;
    box-shadow: 0 10px 30px rgba(0,0,0,0.35);
  }
  .card-front { left: 40px; }
  .card-back { left: 620px; }
  .wave { position: absolute; inset: 0; width: 100%; height: 100%; }
  .front-logo {
    position: absolute;
    left: 38px;
    top: 62px;
    width: 190px;
    font-weight: 800;
    font-size: 27px;
    line-height: 1.1;
    color: var(--copper);
  }
  .divider {
    position: absolute;
    left: 250px;
    top: 96px;
    width: 1px;
    height: 150px;
    background: var(--copper);
  }
  .contact-block {
    position: absolute;
    left: 268px;
    top: 92px;
    color: var(--text);
  }
  .person-name {
    font-weight: 700;
    font-size: 19px;
    color: var(--copper);
    letter-spacing: 0.2px;
    text-transform: uppercase;
  }
  .person-title { font-size: 12.5px; margin-bottom: 14px; }
  .contact-list { list-style: none; }
  .contact-item {
    display: flex;
    align-items: center;
    gap: 6px;
    font-size: 11.5px;
    line-height: 19px;
  }
  .contact-icon { width: 11px; height: 11px; flex: none; }
  .back-logo {
    position: absolute;
    inset: 0;
    display: flex;
    align-items: center;
    justify-content: center;
    text-align: center;
    font-weight: 800;
    font-size: 52px;
    line-height: 1.05;
    color: var(--copper);
  }
</style>
</head>
<body>
  <section class="card card-front">
    <svg class="wave" viewBox="0 0 540 320" aria-hidden="true">
      <path d="M0,96 C18,210 90,262 210,272 C330,282 410,292 470,320 L0,320 Z" fill="var(--ink)"/>
      <path d="M8,70 C26,196 100,250 214,260 C340,270 420,282 492,320" fill="none" stroke="var(--copper)" stroke-width="3"/>
    </svg>
    <div class="front-logo">Brindle Gardenworks</div>
    <div class="divider"></div>
    <div class="contact-block">
      <div class="person-name">Marcus Hale</div>
      <div class="person-title">Managing Director</div>
      <ul class="contact-list">
        <li class="contact-item">
          <svg class="contact-icon" viewBox="0 0 12 12"><path d="M2.5 1 L4.5 1 L5.2 3.6 L4 4.6 C4.6 6 6 7.4 7.4 8 L8.4 6.8 L11 7.5 L11 9.5 C11 10.3 10.3 11 9.5 11 C5 11 1 7 1 2.5 C1 1.7 1.7 1 2.5 1 Z" fill="var(--copper)"/></svg>
          5127730194
        </li>
        <li class="contact-item">
          <svg class="contact-icon" viewBox="0 0 12 12"><rect x="1" y="2.5" width="10" height="7" fill="var(--copper)"/><path d="M1 2.5 L6 6.5 L11 2.5" fill="none" stroke="#fff" stroke-width="1"/></svg>
          brindlegardenworks@mailnest.example
        </li>
        <li class="contact-item">
          <svg class="contact-icon" viewBox="0 0 12 12"><circle cx="6" cy="6" r="5" fill="var(--copper)"/><path d="M1 6 H11 M6 1 C3.5 3.5 3.5 8.5 6 11 M6 1 C8.5 3.5 8.5 8.5 6 11" fill="none" stroke="#fff" stroke-width="0.8"/></svg>
          www.brindlegardenworks.example
        </li>
        <li class="contact-item">
          <svg class="contact-icon" viewBox="0 0 12 12"><rect x="1" y="1" width="10" height="10" rx="3" fill="none" stroke="var(--copper)" stroke-width="1.3"/><circle cx="6" cy="6" r="2.2" fill="none" stroke="var(--copper)" stroke-width="1.3"/></svg>
          @brindlegardenworksrvt
        </li>
      </ul>
    </div>
  </section>

  <section class="card card-back">
    <div class="back-logo">Brindle<br>Gardenworks</div>
  </section>
</body>
</html>
```